Skincare Cleanser Bottle Label

New product launch of a mint facial cleanser.
Brand is called Dorvella.
Product will be called Lumora.
Looking for a label design that can be printed using silk screening.
High gloss white plastic bottle. 8oz. White push pump top.
Clinical skincare brand, professional image, sold in medical spas.

Target Market(s)

Women Age 20-65

Industry/Entity Type

Health And Wellness

Font styles to use
Serif
Sans Serif

Requirements
Must have
• Dorvella brand name in the orignal font.
Should not have
• Multiple colours.

```html
<!DOCTYPE html>
<html lang="en">
<head>
<meta charset="utf-8">
<title>Dorvella Lumora Mint Facial Cleanser Label</title>
<link rel="stylesheet" href="https://fonts.googleapis.com/css2?family=Comfortaa:wght@400&family=Roboto:wght@400;500&family=Didact+Gothic&display=swap">
<style>
  :root {
    --ink: #111111;
    --band: #4a4a4a;
    --title: #3c3c3c;
    --paper: #ffffff;
    --silver-light: #fbfbfb;
    --silver-mid: #e6e6e6;
    --silver-dark: #c9c9c9;
    --leaf-light: #6cc24a;
    --leaf-dark: #2f7d22;
  }
  * { margin: 0; padding: 0; box-sizing: border-box; }
  html, body { width: 738px; height: 1200px; overflow: hidden; background: var(--paper); }
  .canvas { position: relative; width: 738px; height: 1200px; background: var(--paper); }
  .label { position: absolute; left: 155px; top: 0; width: 428px; height: 1200px; }

  .brand {
    position: absolute; top: 52px; left: 0; width: 100%;
    text-align: center;
    font-family: "Comfortaa", sans-serif; font-weight: 400;
    font-size: 44px; letter-spacing: 1px; color: var(--ink);
  }
  .product-name {
    position: absolute; top: 232px; left: 0; width: 100%;
    text-align: center;
    font-family: "Roboto", sans-serif; font-weight: 500;
    font-size: 82px; line-height: 1; color: var(--ink);
  }
  .band { position: absolute; top: 295px; left: 0; width: 428px; height: 127px; }
  .band path { fill: var(--band); }

  .descriptor {
    position: absolute; top: 414px; left: 55px;
    font-family: "Roboto", sans-serif; font-weight: 400;
    font-size: 80px; line-height: 86px; color: var(--title);
  }
  .info-panel {
    position: absolute; top: 703px; left: 0; width: 428px; height: 147px;
    background: linear-gradient(90deg, var(--silver-dark), var(--silver-light) 30%, var(--silver-mid) 60%, var(--silver-light) 80%, var(--silver-dark));
    border-top: 3px solid var(--silver-mid);
    border-bottom: 3px solid var(--silver-dark);
    display: flex; align-items: center; justify-content: center;
    text-align: center;
    font-family: "Didact Gothic", sans-serif; font-size: 15.5px; line-height: 30px; color: var(--ink);
  }
  .mint-leaf {
    position: absolute; top: 892px; left: 87px; width: 248px; height: 190px;
    border-radius: 50% 45% 50% 40%;
    background: radial-gradient(ellipse at 45% 40%, var(--leaf-light), var(--leaf-dark));
  }
  .volume {
    position: absolute; top: 1126px; left: 0; width: 100%;
    text-align: center;
    font-family: "Roboto", sans-serif; font-size: 22px; color: var(--title);
  }
</style>
</head>
<body>
<div class="canvas">
  <div class="label">
    <div class="brand">dorvella</div>
    <div class="product-name">LUMORA</div>
    <svg class="band" viewBox="0 0 428 127" aria-hidden="true">
      <path d="M0 0 Q214 60 428 0 L428 127 Q214 60 0 127 Z"/>
    </svg>
    <div class="descriptor">Mint<br>Facial<br>Cleanser</div>
    <div class="info-panel">
      <p>Lorem Ipsum is simply dummy text of the<br>printing and typesetting industry. Lorem Ipsum<br>has been the industry's standard dummy text<br>ever since the 1500s.</p>
    </div>
    <div class="mint-leaf" role="img" aria-label="Sprig of fresh green mint leaves"></div>
    <div class="volume">8 OZ</div>
  </div>
</div>
</body>
</html>
```